Real Estate "For Sale" Sign for construction company

We need a sign that we can use to hang on a post and place on the road when we sell a property. The sign will be simple and will need to mainly feature our logo (files attached), as well as the words "For Sale", and then our phone number "(555) 417 3968". The sign will hang on a post that'll look something like the attached picture.

Target Market(s)

Home buyers

Industry/Entity Type

Real Estate

Font styles to use
Serif
Sans Serif

Colors
0054AA
0677BA
7BADD7
CADEEF
E8F1F8
0094D4
00A9DD
6FCCEA
C7EBF8
E9F6FB

Requirements
Must have
• For Sale & our phone number

```html
<!DOCTYPE html>
<html lang="en">
<head>
<meta charset="utf-8">
<title>Ridgeline Valley Properties – For Sale Sign</title>
<link rel="stylesheet" href="https://fonts.googleapis.com/css2?family=Montserrat:wght@500&family=Oswald:wght@500&family=Roboto:wght@400&display=swap">
<style>
  :root {
    --backdrop: #424242;
    --sign-white: #ffffff;
    --panel-fill: #c9ebfa;
    --frame-line: #93aacb;
    --brand-blue: #1a7fc1;
    --band-top: #355fae;
    --band-bottom: #1a3a80;
    --ink-navy: #14204a;
    --mark-blue: #0677ba;
  }
  * { margin: 0; padding: 0; box-sizing: border-box; }
  html, body {
    width: 1200px;
    height: 1200px;
    overflow: hidden;
    background: var(--backdrop);
  }
  .sign {
    position: absolute;
    left: 233px;
    top: 50px;
    width: 734px;
    height: 1100px;
    background: var(--sign-white);
  }
  .sign__panel {
    position: absolute;
    inset: 24px;
    background: var(--panel-fill);
    border: 4px solid var(--frame-line);
  }
  .brand {
    position: absolute;
    left: 0;
    right: 0;
    top: 92px;
    text-align: center;
    color: var(--brand-blue);
    font-family: "Montserrat", sans-serif;
    font-weight: 500;
  }
  .brand__dot {
    display: block;
    width: 96px;
    height: 96px;
    margin: 0 auto 18px;
    border-radius: 50%;
    background: var(--mark-blue);
  }
  .brand__name {
    font-size: 50px;
    line-height: 1;
    letter-spacing: 0.5px;
  }
  .brand__tagline {
    margin-top: 14px;
    font-size: 14px;
    letter-spacing: 21px;
    padding-left: 21px;
    line-height: 1;
  }
  .sale-band {
    position: absolute;
    left: 0;
    right: 0;
    top: 452px;
    height: 196px;
    background: linear-gradient(180deg, var(--band-top) 0%, var(--band-top) 30%, var(--band-bottom) 100%);
    display: flex;
    align-items: center;
    justify-content: center;
  }
  .sale-band::before,
  .sale-band::after {
    content: "";
    position: absolute;
    top: 0;
    bottom: 0;
    width: 4px;
    background: rgba(201, 222, 239, 0.55);
  }
  .sale-band::before { left: 24px; }
  .sale-band::after { right: 24px; }
  .sale-band__text {
    color: var(--sign-white);
    font-family: "Oswald", sans-serif;
    font-weight: 500;
    font-size: 184px;
    line-height: 1;
    letter-spacing: 3px;
    transform: translateY(-4px);
  }
  .phone {
    position: absolute;
    left: 0;
    right: 0;
    top: 895px;
    text-align: center;
    color: var(--ink-navy);
    font-family: "Roboto", sans-serif;
    font-weight: 400;
    font-size: 92px;
    line-height: 1;
    letter-spacing: -1px;
  }
</style>
</head>
<body>
  <main class="sign">
    <div class="sign__panel"></div>

    <header class="brand">
      <span class="brand__dot"></span>
      <div class="brand__name">Ridgeline Valley</div>
      <div class="brand__tagline">PROPERTIES</div>
    </header>

    <section class="sale-band">
      <h1 class="sale-band__text">FOR SALE</h1>
    </section>

    <p class="phone">(555) 417 3968</p>
  </main>
</body>
</html>
```